Design an Outstanding flyer for my company.

I need a flyer designed for our window tinting company based in Brisbane Queensland Australia. The flyer will be targeting Home tinting. We also do mobile car tinting. Something in regards to this could be incorporated into the flyer as well.
I want it to be 2 sided DL size. Black background.
It really needs to Pop, and be a real attention getter.
It needs to be easy to read.
I have provided a mock up with the info on it from our marketing company. It will need a spellcheck etc to make sure everything is correct.
Everything about it can be changed however you like.
I have also included the company logo.

Lets see what you've got!

Target Market(s)

Home Owners

Industry/Entity Type

Home Improvement

Font styles to use
Other font styles liked:
• Duan Penh

Requirements
Must have
• All the information on the mock up. Clear and easy to read.
• Must Stand Out!

```html
<!DOCTYPE html>
<html lang="en">
<head>
<meta charset="utf-8">
<title>SunLine Home Window Tinting – DL Flyer</title>
<link rel="stylesheet" href="https://fonts.googleapis.com/css2?family=Roboto:wght@400;700&display=swap">
<style>
  :root {
    --yellow: #fcdb1c;
    --red: #ac1f25;
    --black: #0b0b0b;
    --white: #ffffff;
    --backdrop: #e4e5e7;
  }
  * { box-sizing: border-box; margin: 0; padding: 0; }
  html, body {
    width: 1200px; height: 1200px; overflow: hidden;
    background: var(--backdrop);
    font-family: "Roboto", Arial, sans-serif;
  }
  .flyer {
    position: absolute;
    width: 440px; height: 922px;
    background: var(--yellow);
    overflow: hidden;
  }
  .flyer--front { left: 124px; top: 122px; }
  .flyer--back { left: 638px; top: 124px; width: 438px; height: 918px; }

  .side-strip {
    position: absolute; top: 0; right: 0;
    width: 110px; bottom: 0;
    background: var(--red);
  }
  .flyer--back .side-strip { width: 108px; }
  .footer-band {
    position: absolute; left: 0; right: 0; bottom: 0;
    height: 102px; background: var(--black);
    display: flex; align-items: center; justify-content: center; gap: 12px;
  }
  .flyer--back .footer-band { height: 100px; }
  .brand-dot { width: 22px; height: 22px; border-radius: 50%; background: var(--yellow); }
  .brand-name { color: var(--yellow); font-weight: 700; font-size: 30px; letter-spacing: 2px; }

  /* Front: reasons list */
  .reasons { position: absolute; left: 0; top: 10px; width: 330px; list-style: none; }
  .reasons li {
    position: relative; padding-left: 26px;
    font-weight: 700; color: var(--black); white-space: nowrap;
  }
  .reasons li::before {
    content: ""; position: absolute; left: 0; width: 7px; background: var(--red);
  }
  .reasons .major { font-size: 34px; line-height: 36px; margin-bottom: 14px; }
  .reasons .major::before { top: 9px; height: 20px; }
  .reasons .major:last-of-type { margin-bottom: 18px; }
  .reasons .minor { font-size: 20px; line-height: 24px; margin-bottom: 9.6px; letter-spacing: -0.1px; }
  .reasons .minor::before { top: 6px; height: 14px; }

  .strip-heading {
    position: absolute; top: 0; right: 0; width: 110px; height: 820px;
    writing-mode: vertical-rl;
    display: flex; align-items: center; justify-content: center;
    text-align: center;
    color: var(--white); font-weight: 700; font-size: 31px; line-height: 42px;
  }

  /* Back */
  .mobile-box {
    position: absolute; left: 0; top: 17px; width: 310px; height: 267px;
    background: var(--red); border-radius: 0 8px 8px 0;
    padding: 32px 0 0 41px;
    color: var(--white); font-weight: 700; font-size: 36px; line-height: 50px;
  }
  .call-line {
    position: absolute; left: 19px; top: 326px;
    color: var(--red); font-weight: 700; font-size: 46px; line-height: 50px;
  }
  .contact {
    position: absolute; left: 16px; top: 455px; width: 292px;
    border-top: 4px solid var(--black); border-bottom: 4px solid var(--black);
    padding: 14px 0 12px 6px;
    color: var(--red); font-weight: 700; font-size: 29px; line-height: 44px;
  }
  .tagline {
    position: absolute; left: 21px; top: 588px;
    color: var(--red); font-weight: 700; font-size: 44px; line-height: 52px;
  }
  .web-address {
    position: absolute; top: 0; right: 0; width: 108px; height: 818px;
    writing-mode: vertical-rl;
    display: flex; align-items: center; justify-content: center;
    color: var(--white); font-weight: 400; font-size: 46px; line-height: 108px;
  }
</style>
</head>
<body>

<section class="flyer flyer--front" aria-label="Flyer front">
  <ul class="reasons">
    <li class="major">KEEP HEAT OUT</li>
    <li class="major">BLOCK<br>99.9% UV RAYS</li>
    <li class="major">SAVE MONEY</li>
    <li class="major">INCREASE PRIVACY</li>
    <li class="minor">Reduce Glare</li>
    <li class="minor">Reduce Energy Costs</li>
    <li class="minor">Control The Amount Of Light<br>Entering Your House</li>
    <li class="minor">Reduce Carbon Footprint</li>
    <li class="minor">Make Home More Beautiful</li>
    <li class="minor">Eliminate Home Hot Spots</li>
    <li class="minor">Protect Against Broken Glass</li>
    <li class="minor">Protects Upholstery</li>
    <li class="minor">Improves Effectiveness<br>Of Roof Insulation</li>
    <li class="minor">Improve Health</li>
    <li class="minor">Reduces Interior Floor Fading</li>
    <li class="minor">Eliminate Need For Blinds</li>
    <li class="minor">Strengthen Your Windows</li>
    <li class="minor">Insulate In Winters</li>
    <li class="minor">Affordable</li>
  </ul>
  <div class="side-strip"></div>
  <h2 class="strip-heading">20 REASONS WHY<br>HOME WINDOW TINTING IS PERFECT FOR YOU</h2>
  <footer class="footer-band">
    <span class="brand-dot"></span><span class="brand-name">SUNLINE</span>
  </footer>
</section>

<section class="flyer flyer--back" aria-label="Flyer back">
  <div class="mobile-box">MOBILE<br>CAR TINTING<br>ALSO<br>AVAILABLE</div>
  <h2 class="call-line">CALL<br>BRISBANE’S</h2>
  <div class="contact">
    <p>TEL: 07 3100 4820</p>
    <p>SMS: 0400 582 136</p>
  </div>
  <h2 class="tagline">LEADER IN<br>HOME<br>WINDOW<br>TINTING</h2>
  <div class="side-strip"></div>
  <p class="web-address">www.sunlinetinting.com.au</p>
  <footer class="footer-band">
    <span class="brand-dot"></span><span class="brand-name">SUNLINE</span>
  </footer>
</section>

</body>
</html>
```